brightlakePRESS is publishing a new book and needs some exceptional cover and layout design!

We are publishing a narrow niche PDF eBook and need both a great cover AND great magazine style layout.

The eBook is a compilation of interviews with 12 financial experts on a particular topic. So the format is is the same for each interview 'chapter'

We are looking for a good front cover/document design that will make what is a pretty dry topic, exciting, interesting and easy to read. Basically - magazine style layout.

The specs for the front cover are:

Title:

The Hurdles and Openings Before Bookkeepers and Planners In Expanding Their Pension Fund Practice In 2014 -2015

by Tom Vellani

published by brightlakePRESS

The client would like a similar cover to the one I have attached for your reference. (book front cover example). By no means be limited by this design suggestion. The only caveat is that shots of all interview subjects are included (except the author). These have been included in the zip file.

The design for the text should be elegant and consistent with the design of the front cover. Please format the text in pages 1 to 15 to demonstrate you've understood the brief.

Attached files.

1) MS word version of draft book pages 1 to 15
2) copy of the cover my client would like to emulate.

reminder - this is destined to be a PDF eBook - so looking for some nice eye catching magazine style layout in the design. Columns would be fine.

Good luck!

Brent Marlow
brightlakePRESS

Target Market(s)

Professional Accountants who are running there own businesses

Industry/Entity Type

Financial

Colors

Designer to choose colors to be used in the design.

Requirements
Must have
• The cover must feature headshots of all the interview subjects. The PDF layout must be optimised for viewing on an iPad

```html
<!DOCTYPE html>
<html lang="en">
<head>
<meta charset="utf-8">
<title>The Hurdles and Openings Before Bookkeepers and Planners – Tom Vellani</title>
<link rel="stylesheet" href="https://fonts.googleapis.com/css2?family=Noto+Serif:wght@400&display=swap">
<style>
  :root {
    --page: #e6e6e6;
    --frame: #cdcdcd;
    --panel: #f2f2f2;
    --ink: #1c1c1c;
    --photo-a: #8a8580;
    --photo-b: #5d5a57;
  }
  * { margin: 0; padding: 0; box-sizing: border-box; }
  html, body { width: 846px; height: 1200px; overflow: hidden; }
  body {
    background: var(--page);
    font-family: "Noto Serif", Georgia, serif;
    color: var(--ink);
  }
  .cover { position: relative; width: 846px; height: 1200px; overflow: hidden; }

  .frame-top {
    position: absolute; left: 58px; top: -120px; width: 730px; height: 863px;
    background: var(--frame); border-radius: 0 0 104px 104px;
  }
  .panel-top {
    position: absolute; left: 114px; top: 0; width: 618px; height: 685px;
    background: var(--panel); border-radius: 0 0 30px 30px;
    text-align: center;
  }
  .title {
    margin: 132px auto 0; width: 610px;
    font-weight: 400; font-size: 38.5px; line-height: 48.5px;
    letter-spacing: -0.2px;
  }
  .author {
    margin-top: 24px;
    font-weight: 400; font-size: 38px; line-height: 48px;
  }

  .experts {
    position: absolute; left: 208px; top: 757px;
    display: grid; grid-template-columns: repeat(5, 79px);
    gap: 9px;
  }
  .headshot {
    width: 79px; height: 79px;
    background: linear-gradient(180deg, var(--photo-a), var(--photo-b));
  }
  .headshot.light { background: linear-gradient(180deg, #e9e6e2, #9a8f86); }
  .headshot.warm { background: linear-gradient(180deg, #7d8c7a, #5e6a5a); }

  .frame-bottom {
    position: absolute; left: 58px; top: 1029px; width: 730px; height: 300px;
    background: var(--frame); border-radius: 104px 104px 0 0;
  }
  .panel-bottom {
    position: absolute; left: 114px; top: 1086px; width: 618px; height: 200px;
    background: var(--panel); border-radius: 30px 30px 0 0;
    text-align: center;
  }
  .publisher {
    margin-top: 25px;
    font-size: 19px; line-height: 24px;
  }
</style>
</head>
<body>
  <main class="cover">
    <div class="frame-top"></div>
    <header class="panel-top">
      <h1 class="title">The Hurdles and Openings Before Bookkeepers and Planners In Expanding Their Pension Fund Practice In 2014 -2015</h1>
      <p class="author">Tom Vellani</p>
    </header>

    <section class="experts" aria-label="Interview subjects">
      <div class="headshot" role="img" aria-label="Headshot of interview subject 1"></div>
      <div class="headshot" role="img" aria-label="Headshot of interview subject 2"></div>
      <div class="headshot" role="img" aria-label="Headshot of interview subject 3"></div>
      <div class="headshot light" role="img" aria-label="Headshot of interview subject 4"></div>
      <div class="headshot" role="img" aria-label="Headshot of interview subject 5"></div>
      <div class="headshot light" role="img" aria-label="Headshot of interview subject 6"></div>
      <div class="headshot" role="img" aria-label="Headshot of interview subject 7"></div>
      <div class="headshot" role="img" aria-label="Headshot of interview subject 8"></div>
      <div class="headshot warm" role="img" aria-label="Headshot of interview subject 9"></div>
      <div class="headshot light" role="img" aria-label="Headshot of interview subject 10"></div>
      <div class="headshot light" role="img" aria-label="Headshot of interview subject 11"></div>
      <div class="headshot" role="img" aria-label="Headshot of interview subject 12"></div>
      <div class="headshot light" role="img" aria-label="Headshot of interview subject 13"></div>
      <div class="headshot light" role="img" aria-label="Headshot of interview subject 14"></div>
      <div class="headshot light" role="img" aria-label="Headshot of interview subject 15"></div>
    </section>

    <div class="frame-bottom"></div>
    <footer class="panel-bottom">
      <p class="publisher">Published by brightlakePRESS</p>
    </footer>
  </main>
</body>
</html>
```